Custom Manufacturing Job Shop

We are looking for a business card design for Tall Oak Fabrication Inc. Tall Oak is a family owned business that manufactures any custom product to fit a customers needs, whether it is custom 1 piece or production parts, we truly take on projects that others just cant do. to help in your design go to www.talloakfab.example for a more in depth idea. we have the following capabilities that we would like to see on the card somewhere...maybe on the back of a 2 sided card? we are fully open to ideas.
Machining
• Fabrication
• Millwork
• Maintenance
• Laser Cutting
• Precision Forming
Engineering
Blasting/Painting

No matter how big or small, We literally do it all

preferably black or darker cards but we don't mind to see some color if you see a better fit. we are interested in looking at anything that catches attention.
I have attached our logo, if it is needed in a different file type please let me know and I will send it to you if I can. maybe adding some type of drawing or dimensional lines would be something to add?? just throwing ideas out there....

Reason: I added one of our shredder designs and would like to see a few more cards if possible using this. any questions please don't hesitate to ask!!

Target Market(s)

anyone looking for design/manufacturing/machining whether it is custom 1 off parts or production.

Industry/Entity Type

Business

Contact Information for Business Card

preferably darker shades, but also not opposed to some color in the same sense....not too bright

Font styles to use
Serif
Sans Serif

Requirements
Must have
• Dell Marwick
• Direct:555-213-7790
• Cell:555-348-1162
• Fax: 555-907-4425
• 42 Quarry Lane
• Klingerstown, PA 00000
• I also would request having it in a format I can give to the company making the business cards to edit names/numbers etc. for the entire staff.
Nice to have
• drafting lines? we are open to almost anything....
Should not have
• exotic colors

```html
<!DOCTYPE html>
<html lang="en">
<head>
<meta charset="utf-8">
<title>Tall Oak Fabrication – Capabilities</title>
<link rel="stylesheet" href="https://fonts.googleapis.com/css2?family=Arimo:wght@400&display=swap">
<style>
  :root {
    --sky: #5272ba;
    --steel: #3f5180;
    --slate: #262c3c;
    --night: #040406;
    --rule: #d8dce6;
    --ink: #ffffff;
    --mark: #dcdcdc;
  }
  html, body {
    margin: 0;
    padding: 0;
    overflow: hidden;
  }
  .card {
    position: relative;
    width: 1200px;
    height: 857px;
    overflow: hidden;
    background: linear-gradient(180deg, var(--sky) 0%, var(--steel) 33%, var(--slate) 60%, var(--night) 100%);
    font-family: "Arimo", Arial, sans-serif;
    color: var(--ink);
  }
  .brand {
    position: absolute;
    top: 92px;
    right: 56px;
    display: flex;
    align-items: center;
    gap: 16px;
    color: var(--mark);
    font-size: 50px;
    letter-spacing: 1px;
    text-transform: uppercase;
  }
  .brand-square {
    width: 40px;
    height: 40px;
    background: var(--mark);
  }
  .divider {
    position: absolute;
    top: 225px;
    left: 73px;
    width: 1084px;
    height: 1px;
    background: var(--rule);
  }
  .capabilities {
    position: absolute;
    top: 275px;
    left: 171px;
    margin: 0;
    padding: 0;
    list-style: none;
    font-size: 36px;
    line-height: 66.5px;
  }
  .capabilities .bullet::before {
    content: "•";
    margin-right: 7px;
  }
  .capabilities .plain {
    padding-left: 23px;
  }
</style>
</head>
<body>
  <main class="card">
    <div class="brand">
      <span class="brand-square"></span>
      <span class="brand-name">Tall Oak</span>
    </div>
    <div class="divider"></div>
    <ul class="capabilities">
      <li class="bullet">Fabrication</li>
      <li class="bullet">Millwork</li>
      <li class="bullet">Maintenance</li>
      <li class="bullet">Laser Cutting</li>
      <li class="bullet">Precision Forming</li>
      <li class="plain">Engineering</li>
      <li class="plain">Blasting/Painting</li>
    </ul>
  </main>
</body>
</html>
```